Pricing Page; Request Quote Page Design

I'm looking to update our pricing page and request page to something more modern in terms of the layout/form design and with more content, but needs to be consistent with the rest of our site. I need two pages designed. 1) A general pricing page w/ CTAs for quotes, and 2) The request quote page with form. Ideally there would be (3) parts for our different packages (Express, Professional, Enterprise) on the pricing page, with CTAs on each section. I like the hero image approach used here https://plovane.com/pricing and here http://www.gridmarrow.com/wp-content/uploads/2016/08/corvalink-pricing-page-design.png In terms of the form page, mainly just looking for an improvement over this https://www.lumadrift.com/price-quote-request

I also included a sample mockup to provide a BIT of guidance, but looking for something a little different and modern.

Industry/Entity Type

Pricing

Number of Pages Required

2 page

Font styles to use
Sans Serif

Requirements
Must have
• Hero background image on main pricing page. Needs to follow the look and feel of lumadrift.com

```html
<!DOCTYPE html>
<html lang="en">
<head>
<meta charset="utf-8">
<title>Pricing — Lumadrift</title>
<link rel="stylesheet" href="https://fonts.googleapis.com/css2?family=Open+Sans:wght@300;400;600&family=Raleway:wght@500&display=swap">
<style>
  :root {
    --green: #8cc63f;
    --green-soft: #b0d878;
    --teal: #58bfc0;
    --teal-soft: #8ad4d2;
    --white: #ffffff;
    --ink: #333333;
    --footer: #0a0a0a;
    --photo-dark: #151718;
    --photo-mid: #4a4d50;
    --photo-light: #6c6f72;
    --photo-warm: #5a524a;
  }
  * { box-sizing: border-box; margin: 0; padding: 0; }
  html, body { width: 1200px; height: 926px; overflow: hidden; }
  body { position: relative; font-family: "Open Sans", Arial, sans-serif; color: var(--white); background: var(--footer); }

  .hero { position: absolute; left: 0; top: 0; width: 1200px; height: 810px; }
  .hero-photo {
    position: absolute; inset: 0;
    background:
      radial-gradient(ellipse 420px 300px at 30% 30%, rgba(108,111,114,0.55), transparent 70%),
      radial-gradient(ellipse 380px 260px at 75% 20%, rgba(130,134,138,0.45), transparent 70%),
      radial-gradient(ellipse 300px 260px at 15% 75%, rgba(90,82,74,0.55), transparent 70%),
      radial-gradient(ellipse 320px 280px at 92% 65%, rgba(74,77,80,0.6), transparent 70%),
      linear-gradient(160deg, var(--photo-mid) 0%, #35383b 45%, var(--photo-dark) 100%);
  }
  .hero-shade { position: absolute; inset: 0; background: rgba(10,12,14,0.45); }

  .brand { position: absolute; left: 89px; top: 52px; height: 28px; display: flex; align-items: center; gap: 10px; }
  .brand-mark { width: 14px; height: 14px; background: var(--white); }
  .brand-name { font-weight: 600; font-size: 20px; color: var(--white); }

  .utility { position: absolute; right: 88px; top: 17px; display: flex; align-items: center; gap: 16px; }
  .utility-phone { font-size: 14px; }
  .btn-demo { display: block; background: var(--green); color: var(--white); font-size: 11.5px; padding: 8px 8px; border-radius: 2px; text-decoration: none; }

  .main-nav { position: absolute; right: 88px; top: 66px; display: flex; gap: 36px; }
  .main-nav a { color: var(--white); text-decoration: none; font-size: 13.5px; }

  .hero-copy { position: absolute; left: 0; width: 1200px; top: 190px; text-align: center; }
  .hero-title { font-weight: 600; font-size: 31px; letter-spacing: 0.3px; }
  .hero-lead { margin: 12px auto 0; width: 720px; font-size: 17.5px; line-height: 28px; }

  .plans { position: absolute; top: 408px; left: 159px; display: flex; gap: 28px; }
  .plan { width: 276px; }
  .plan-name { height: 41px; line-height: 43px; text-align: center; font-size: 18px; font-weight: 400; border-radius: 2px 2px 0 0; }
  .plan-price { position: relative; height: 105px; display: flex; justify-content: center; align-items: flex-end; padding-bottom: 20px; }
  .plan-price::after {
    content: ""; position: absolute; left: 50%; bottom: -5px; margin-left: -5px;
    border-left: 5px solid transparent; border-right: 5px solid transparent; border-top: 5px solid var(--tone-soft);
  }
  .currency { font-size: 24px; font-weight: 400; align-self: flex-start; margin-top: 18px; margin-right: 2px; }
  .amount { font-size: 76px; font-weight: 400; line-height: 62px; }
  .period { font-size: 15px; margin-left: 4px; margin-bottom: 0; }
  .plan-body { position: relative; background: var(--white); color: var(--ink); height: 152px; padding: 30px 20px 0; font-size: 13.1px; line-height: 22px; text-align: justify; text-align-last: center; }
  .plan-body::after {
    content: ""; position: absolute; left: 50%; bottom: 0; margin-left: -5px;
    border-left: 5px solid transparent; border-right: 5px solid transparent; border-bottom: 5px solid var(--tone);
  }
  .plan-cta { display: block; height: 37px; line-height: 38px; text-align: center; color: var(--white); font-size: 17px; text-decoration: none; border-radius: 0 0 2px 2px; }

  .plan--express, .plan--enterprise { --tone: var(--green); --tone-soft: var(--green-soft); }
  .plan--professional { --tone: var(--teal); --tone-soft: var(--teal-soft); }
  .plan-name, .plan-cta { background: var(--tone); }
  .plan-price { background: var(--tone-soft); }

  .site-footer { position: absolute; left: 0; top: 810px; width: 1200px; height: 116px; background: var(--footer); }
  .footer-nav { position: absolute; left: 91px; top: 32px; width: 460px; display: flex; flex-wrap: wrap; column-gap: 19px; row-gap: 1px; font-family: "Raleway", Arial, sans-serif; }
  .footer-nav a { color: #e6e6e6; text-decoration: none; font-size: 13.5px; line-height: 18px; }
  .legal { position: absolute; left: 851px; top: 37px; font-size: 7.5px; color: #bbbbbb; }
  .legal a { color: var(--green); text-decoration: none; }
  .chat-btn { position: absolute; left: 1070px; top: 34px; width: 42px; height: 41px; background: var(--green); border-radius: 2px; display: flex; align-items: center; justify-content: center; }
</style>
</head>
<body>
  <header class="hero">
    <div class="hero-photo" role="img" aria-label="Hero background photo: overhead view of a work desk with laptop, keyboard, camera, coffee cup, notebooks and a planner"></div>
    <div class="hero-shade"></div>

    <div class="brand"><span class="brand-mark"></span><span class="brand-name">Lumadrift</span></div>

    <div class="utility">
      <span class="utility-phone">CALL 1-866-555-0142</span>
      <a class="btn-demo" href="#">REQUEST DEMO</a>
    </div>

    <nav class="main-nav">
      <a href="#">FEATURES</a><a href="#">SERVICES</a><a href="#">PRICING</a><a href="#">RESOURCES</a><a href="#">BLOG</a><a href="#">NEWS</a><a href="#">CONTACT</a>
    </nav>

    <div class="hero-copy">
      <h1 class="hero-title">Flexible Pricing Designed to Fit Your Business</h1>
      <p class="hero-lead">Our pay-as-you-grow pricing model is geared to minimize risk and maximize return. Whether launching a new learning initiative, or looking to migrate (or integrate) an existing business with our Learning Business Platform, we have you covered.</p>
    </div>

    <section class="plans">
      <article class="plan plan--express">
        <h2 class="plan-name">EXPRESS</h2>
        <div class="plan-price"><span class="currency">$</span><span class="amount">20</span><span class="period">/ mo.</span></div>
        <p class="plan-body">Launch in weeks, not months. Perfect for smaller businesses with less than 1,000 users and requiring less than 25 courses. Packages start at $499.</p>
        <a class="plan-cta" href="#">Request Quote</a>
      </article>
      <article class="plan plan--professional">
        <h2 class="plan-name">PROFESSIONAL</h2>
        <div class="plan-price"><span class="currency">$</span><span class="amount">30</span><span class="period">/ mo.</span></div>
        <p class="plan-body">Designed for more established learning businesses which are need to scale and leverage modern technology. Up to 10k users &amp; 100 courses.</p>
        <a class="plan-cta" href="#">Request Quote</a>
      </article>
      <article class="plan plan--enterprise">
        <h2 class="plan-name">ENTERPRISE</h2>
        <div class="plan-price"><span class="currency">$</span><span class="amount">50</span><span class="period">/ mo.</span></div>
        <p class="plan-body">For larger organizations needing to scale learning globally to more than 10,000 users, with hundreds of courses and multiple instances.</p>
        <a class="plan-cta" href="#">Request Quote</a>
      </article>
    </section>
  </header>

  <footer class="site-footer">
    <nav class="footer-nav">
      <a href="#">Features</a><a href="#">Services</a><a href="#">Pricing</a><a href="#">Resources</a><a href="#">Blog</a><a href="#">News</a><a href="#">Careers</a><a href="#">Contact</a>
    </nav>
    <p class="legal">Copyright © 2016 Lumadrift, Inc. &nbsp;|&nbsp; <a href="#">Privacy Policy</a></p>
    <a class="chat-btn" href="#" aria-label="Chat">
      <svg width="22" height="20" viewBox="0 0 22 20" fill="none" stroke="#ffffff" stroke-width="1.6" stroke-linejoin="round">
        <path d="M7 2h13v9h-3v3l-3-3H7z"/>
        <path d="M7 7H2v8h2v3l3-3h5v-4"/>
      </svg>
    </a>
  </footer>
</body>
</html>
```